Out of town New Masters of Accounting

size of ad is 7” x 9.6”
please leave one inch on bottom for footer
We want to attract out of town students to join this master's in accounting program.
You DO NOT  have to use a picture of a person.
But if you do, it should be a  male with a white shirt and should not have long hair.(look like a young executive)
THE TEXT OF THE AD IS IN THE ATTACHMENTS
THE CAP LETTERS ARE THE INSTRUCTIONS

The age we are trying to attract is from 20-30 of ages.
- a clear ad .. the text should not take up the entire ad.. it should not be very crowded -
it should be an attractive ad that people would want to see and stand out
- the text very big and take up the entire ad

```html
<!DOCTYPE html>
<html lang="en">
<head>
<meta charset="utf-8">
<title>Out of Town Masters in Accounting</title>
<link rel="stylesheet" href="https://fonts.googleapis.com/css2?family=Roboto+Condensed:wght@700&family=Kaushan+Script&family=Questrial&family=Arimo:wght@400;700&display=swap">
<style>
  :root {
    --stage: #a5a5a5;
    --paper: #ffffff;
    --orange: #e5730f;
    --yellow: #ebb30c;
    --gold: #c99b12;
    --ink: #4a4a4c;
    --burst: #f6b21f;
    --black: #111111;
    --photo-dark: #3c3c3c;
    --photo-light: #b9b9b9;
  }
  * { margin: 0; padding: 0; box-sizing: border-box; }
  html, body { width: 1200px; height: 1200px; overflow: hidden; background: var(--stage); }
  .flyer {
    position: absolute; left: 162px; top: 0;
    width: 876px; height: 1200px; background: var(--paper); overflow: hidden;
  }
  .flyer-shapes { position: absolute; inset: 0; }
  .txt { position: absolute; white-space: nowrap; }
  .all-new {
    left: 28px; top: 322px; font-family: "Kaushan Script", cursive;
    font-size: 82px; color: var(--paper); line-height: 1;
  }
  .remote {
    left: 25px; top: 424px; font-family: "Questrial", sans-serif;
    font-size: 32px; line-height: 38px; color: var(--paper);
  }
  .cond { font-family: "Roboto Condensed", sans-serif; font-weight: 700; }
  .start-date { left: 27px; top: 550px; font-size: 48px; color: var(--paper); line-height: 1; }
  .lower-prices { left: 520px; top: 590px; font-size: 39px; color: var(--paper); line-height: 1; }
  .headline {
    left: 26px; top: 670px; font-size: 86px; line-height: 75px;
    color: var(--ink); letter-spacing: -0.5px;
  }
  .headline .hl { color: var(--orange); }
  .degree-box {
    position: absolute; left: 28px; top: 836px; width: 644px; height: 58px;
    background: var(--ink); color: var(--paper);
    font-family: "Questrial", sans-serif; font-size: 36px;
    display: flex; align-items: center; justify-content: center;
  }
  .advantage { left: 27px; top: 905px; font-size: 33px; color: var(--orange); line-height: 1.2; }
  .facts {
    position: absolute; left: 28px; top: 966px; list-style: none;
    font-family: "Arimo", sans-serif; font-size: 19.5px; line-height: 26.5px; color: var(--black);
  }
  .facts li { padding-left: 21px; position: relative; }
  .facts li::before {
    content: ""; position: absolute; left: 2px; top: 7px;
    width: 7px; height: 7px; border-radius: 50%; background: var(--orange);
  }
  .web {
    left: 27px; top: 1084px; font-family: "Questrial", sans-serif;
    font-size: 25px; color: var(--paper); line-height: 1;
  }
  .web b { font-weight: 700; font-family: "Arimo", sans-serif; }
  .burst-lead {
    left: 596px; top: 1030px; width: 220px; text-align: center;
    font-family: "Questrial", sans-serif; font-size: 24px; line-height: 27px; color: var(--paper);
  }
  .burst-big { left: 600px; top: 1088px; font-size: 52px; color: var(--paper); line-height: 1; }
</style>
</head>
<body>
<main class="flyer">
  <svg class="flyer-shapes" width="876" height="1200" viewBox="0 0 876 1200">
    <defs>
      <linearGradient id="photoTone" x1="0" y1="0" x2="1" y2="1">
        <stop offset="0" stop-color="var(--photo-light)"/>
        <stop offset="1" stop-color="var(--photo-dark)"/>
      </linearGradient>
      <linearGradient id="fadeTone" x1="1" y1="0" x2="0" y2="0">
        <stop offset="0" stop-color="#dcdcdc"/>
        <stop offset="1" stop-color="#ffffff"/>
      </linearGradient>
    </defs>

    <rect class="top-fade" x="0" y="0" width="876" height="294" fill="url(#fadeTone)" role="img" aria-label="Faded classroom photo behind the header"/>

    <circle class="ranking-badge" cx="167" cy="150" r="62" fill="var(--yellow)"/>

    <rect class="orange-band" x="0" y="294" width="876" height="272" fill="var(--orange)"/>

    <circle class="photo-ring" cx="680" cy="227" r="318" fill="var(--paper)"/>
    <circle class="photo" cx="680" cy="227" r="311" fill="url(#photoTone)" role="img" aria-label="Group of young students working together on laptops"/>

    <rect class="price-bar-edge" x="475" y="566" width="401" height="8" fill="var(--paper)"/>
    <rect class="price-bar" x="475" y="574" width="401" height="73" fill="var(--gold)"/>
    <polygon class="price-fold" points="475,616 506,616 475,647" fill="var(--black)"/>

    <rect class="date-bar-edge" x="0" y="536" width="512" height="30" fill="var(--paper)"/>
    <rect class="date-bar" x="0" y="540" width="506" height="77" fill="var(--yellow)"/>

    <circle class="faint-badge" cx="815" cy="805" r="82" fill="var(--yellow)" opacity="0.18"/>

    <polygon class="url-bar" points="0,1071 414,1071 396,1125 0,1125" fill="var(--orange)"/>

    <g class="social">
      <circle cx="42" cy="1158" r="15" fill="var(--ink)"/>
      <circle cx="79" cy="1158" r="15" fill="var(--ink)"/>
      <circle cx="116" cy="1158" r="15" fill="var(--ink)"/>
      <circle cx="156" cy="1158" r="15" fill="var(--ink)"/>
    </g>

    <polygon class="corner-wedge" points="876,1045 876,1200 760,1200" fill="var(--orange)"/>
    <polygon class="burst-shadow" fill="var(--black)" points="681,940 721,1006 778,959 784,1016 876,979 824,1056 876,1096 814,1126 876,1176 820,1200 644,1200 584,1171 460,1190 539,1136 400,1146 514,1101 494,1071 554,1056 584,1006 644,1006"/>
    <polygon class="burst" fill="var(--burst)" points="687,944 727,1010 784,963 790,1020 876,985 830,1060 876,1100 820,1130 876,1180 826,1200 650,1200 590,1175 470,1190 545,1140 410,1144 520,1105 500,1075 560,1060 590,1010 650,1010"/>
  </svg>

  <div class="txt all-new">All new!</div>
  <div class="txt remote">Remote program For<br>out of town students</div>

  <div class="txt cond start-date">BEGINNING AUGUST 17</div>
  <div class="txt cond lower-prices">NEW LOWER PRICES</div>

  <h1 class="txt cond headline">ADVANCE <span class="hl">FURTHER</span> IN<br><span class="hl">YOUR CAREER</span> WITH A</h1>
  <div class="degree-box">Masters of science in accounting</div>

  <div class="txt cond advantage">Harbor Career Alliance Job Placement Advantage</div>
  <ul class="facts">
    <li>96% placement rate</li>
    <li>8 placement coordinators</li>
    <li>Decades of relationships with 100’s of firm</li>
  </ul>

  <div class="txt web">www.<b>gradpath-masters</b>.com</div>

  <div class="txt burst-lead">A masters<br>in only</div>
  <div class="txt cond burst-big">15 months</div>
</main>
</body>
</html>
```